Crimson Vantage Cleaning Solutions

Need a logo and business card design. I want to use a translucent business card. I want to abbreviate the name C.V.C.S. Commercial Cleaning, because my is Dov. I’d also like to incorporate a knight or something like that. I want the idea to tie in with the word Crimson. New ideas are welcome, i don’t want to limit anyone’s creativity.

Target Market(s)

Commercial Cleaning for businesses.

Contact Information for Business Card

Crimson
Vantage
Cleaning
Solutions

```html
<!DOCTYPE html>
<html lang="en">
<head>
<meta charset="utf-8">
<title>Crimson Vantage Cleaning Solutions – Business Cards</title>
<link href="https://fonts.googleapis.com/css2?family=Poppins:wght@400;600;700&family=Roboto:wght@400&display=swap" rel="stylesheet">
<style>
  :root {
    --stage: #232323;
    --card: #ffffff;
    --navy: #23357e;
    --sky: #1fa3df;
    --leaf: #3cb54a;
    --grey: #7a7a7a;
    --mist: #e6f3fb;
  }
  * { box-sizing: border-box; margin: 0; padding: 0; }
  html, body { width: 1200px; height: 1200px; overflow: hidden; background: var(--stage); }
  .stage { position: relative; width: 1200px; height: 1200px; }

  .card {
    position: absolute; left: 150px; width: 900px; height: 514px;
    background: var(--card); border-radius: 22px; overflow: hidden;
    box-shadow: 0 10px 30px rgba(0,0,0,.45);
  }
  .card--front { top: 60px; }
  .card--back { top: 626px; }

  .brand { position: absolute; display: flex; align-items: center; gap: 22px; }
  .brand__dot {
    width: 110px; height: 110px; border-radius: 50%;
    background: linear-gradient(160deg, #bfe6f8, var(--sky));
    flex: none;
  }
  .brand__name {
    font-family: "Poppins", sans-serif; font-weight: 700;
    font-size: 38px; line-height: 1.05; color: var(--navy);
  }
  .brand__tagline {
    font-family: "Poppins", sans-serif; font-weight: 400;
    font-size: 15px; color: var(--grey); margin-top: 8px; letter-spacing: .3px;
  }
  .card--front .brand { left: 50%; top: 50%; transform: translate(-50%, -50%); }
  .card--back .brand { left: 40px; top: 44px; }

  .faint-mark {
    position: absolute; right: 40px; top: 80px; width: 360px; height: 360px;
    border-radius: 50%; background: var(--sky); opacity: .07;
  }
  .sparkle-field {
    position: absolute; right: 0; bottom: 0; width: 330px; height: 130px;
    background: radial-gradient(ellipse at 70% 70%, rgba(31,163,223,.22), rgba(31,163,223,0) 70%);
  }

  .person { position: absolute; left: 40px; top: 240px; font-family: "Poppins", sans-serif; }
  .person__name { font-weight: 700; font-size: 25px; color: var(--navy); }
  .person__title { font-weight: 400; font-size: 21px; color: var(--sky); margin-top: -2px; }

  .divider {
    position: absolute; left: 30px; right: 40px; top: 318px;
    height: 2px; background: var(--navy);
  }

  .contacts { position: absolute; left: 40px; top: 336px; list-style: none;
    font-family: "Roboto", sans-serif; font-size: 21px; color: var(--navy); }
  .contacts li { display: flex; align-items: center; gap: 14px; height: 34px; }
  .contacts svg { width: 20px; height: 20px; fill: var(--leaf); flex: none; }

  .address {
    position: absolute; right: 60px; top: 338px; text-align: right;
    font-family: "Roboto", sans-serif; font-size: 21px; line-height: 1.6; color: var(--navy);
  }
</style>
</head>
<body>
<main class="stage">

  <section class="card card--front" aria-label="Card front">
    <div class="brand">
      <span class="brand__dot"></span>
      <div>
        <div class="brand__name">Crimson Vantage<br>Cleaning Solutions</div>
        <div class="brand__tagline">C.V.C.S. Commercial Cleaning</div>
      </div>
    </div>
  </section>

  <section class="card card--back" aria-label="Card back">
    <div class="faint-mark"></div>
    <div class="sparkle-field" role="img" aria-label="Scattered blue sparkle accents"></div>

    <div class="brand">
      <span class="brand__dot"></span>
      <div>
        <div class="brand__name">Crimson Vantage<br>Cleaning Solutions</div>
        <div class="brand__tagline">C.V.C.S. Commercial Cleaning</div>
      </div>
    </div>

    <div class="person">
      <div class="person__name">Marcus Ellery</div>
      <div class="person__title">CEO/Founder</div>
    </div>

    <div class="divider"></div>

    <ul class="contacts">
      <li>
        <svg viewBox="0 0 24 24" aria-hidden="true"><path d="M6.6 10.8a15 15 0 0 0 6.6 6.6l2.2-2.2a1 1 0 0 1 1-.25 11.4 11.4 0 0 0 3.6.57 1 1 0 0 1 1 1V20a1 1 0 0 1-1 1A17 17 0 0 1 3 4a1 1 0 0 1 1-1h3.5a1 1 0 0 1 1 1c0 1.25.2 2.45.57 3.57a1 1 0 0 1-.25 1z"/></svg>
        555-304-1187
      </li>
      <li>
        <svg viewBox="0 0 24 24" aria-hidden="true"><path d="M6 2h12v5H6zM3 8h18a2 2 0 0 1 2 2v6h-4v6H5v-6H1v-6a2 2 0 0 1 2-2zm4 8v4h10v-4z"/></svg>
        555-304-1187
      </li>
      <li>
        <svg viewBox="0 0 24 24" aria-hidden="true"><path d="M2 5h20v14H2zm2 2v.5l8 5 8-5V7l-8 5z"/></svg>
        marcus@cvcsclean.com
      </li>
      <li>
        <svg viewBox="0 0 24 24" aria-hidden="true"><path d="M12 2a10 10 0 1 0 0 20 10 10 0 0 0 0-20zm0 2c.9 0 2.2 2 2.8 5H9.2C9.8 6 11.1 4 12 4zM4.3 11h4.6c0 .7 0 1.4.1 2H4.3a8 8 0 0 1 0-2zm.7 4h4.2c.4 1.7 1 3.1 1.7 4A8 8 0 0 1 5 15zm4-6H5a8 8 0 0 1 5.9-4.9C10.1 5 9.5 6.8 9 9zm3 11c-.9 0-2.2-2-2.8-5h5.6c-.6 3-1.9 5-2.8 5zm3-7H9.1a14 14 0 0 1 0-2h5.8a14 14 0 0 1 0 2zm-1.9 6c.7-.9 1.3-2.3 1.7-4H19a8 8 0 0 1-5.9 4zm2-6c.1-.6.1-1.3.1-2h4.6a8 8 0 0 1 0 2zM15 9c-.5-2.2-1.1-4-1.9-4.9A8 8 0 0 1 19 9z"/></svg>
        www.cvcsclean.com
      </li>
    </ul>

    <address class="address" style="font-style:normal">
      1180 Larkspur Street<br>
      Suite 210, Brookfield<br>
      OH 44403
    </address>
  </section>

</main>
</body>
</html>
```